Vantor Business card and stationary
I need double sided standard sized Business Card [3.5" x 2"]
Leave the font with designers creativity
Professional
Dean Holbrek
Director
P.O Box 481, Ferndale Ridge, NSW 1742
dean@vantorbuildco.com.au
www.vantorbuildco.com.au
Builders Lic No: 371506K
ABN: 83207594116
ACN: 207594116
Also please include united Trades Guild Logo in front side of business card.
One Call Gets It All.
Trusted Building Services,
Project Management, New Constructions. Extensions, Renovations, Alterations, Remoulding, Kitchen renovations, Bathroom Renovations, Strata works, Building Maintenance, Insurance works, Fully Licensed & Insured, Member Of RTF, Member Of united Trades Guilds

```html
<!DOCTYPE html>
<html lang="en">
<head>
<meta charset="utf-8">
<title>Vantor Construction – Stationery Concepts</title>
<link href="https://fonts.googleapis.com/css2?family=Montserrat:wght@600;700&family=Open+Sans:wght@400;600&display=swap" rel="stylesheet">
<style>
:root{
  --stage:#2a2a2a;
  --stage-light:#343434;
  --paper:#ffffff;
  --ink:#3a3a3a;
  --muted:#8a8a8a;
  --red:#c8102e;
  --red-dark:#8e0b1f;
  --grey:#b9b9b9;
  --black-card:#111;
}
*{box-sizing:border-box;margin:0;padding:0}
html,body{width:1200px;height:382px;overflow:hidden;background:var(--stage)}
body{font-family:"Open Sans",Arial,sans-serif;color:var(--ink)}
.canvas{position:relative;width:1200px;height:382px;background:radial-gradient(circle at 40% 40%,var(--stage-light),var(--stage) 70%)}
.abs{position:absolute}
.sheet{position:absolute;background:var(--paper);box-shadow:0 2px 6px rgba(0,0,0,.6);overflow:hidden}
.brand{font-family:"Montserrat",Arial,sans-serif;font-weight:700;letter-spacing:.5px;white-space:nowrap}
.caption{position:absolute;font-size:5px;color:#9a9a9a;text-align:center}
.swoosh{position:absolute;left:0;top:0;width:100%;height:100%}

/* hero lockup */
.hero{left:12px;top:48px;width:276px;text-align:center}
.hero .brand{font-size:23px;color:#fff;line-height:1}
.hero .tagline{font-family:"Montserrat",sans-serif;font-weight:600;font-size:12px;color:#fff;letter-spacing:.6px;margin-top:5px;border-top:1px solid #fff;padding-top:4px}
.hero .sub{font-size:7px;color:#bbb;margin-top:6px}

/* business cards */
.card{width:152px;height:82px}
.card .brand{font-size:8px;color:var(--ink)}
.tiny{font-size:4.4px;line-height:1.45;white-space:nowrap}
.name{font-size:6px;font-weight:600;color:var(--red)}
.services{display:grid;grid-template-columns:1fr 1fr;gap:0 4px;padding:8px 8px}
.services span::before{content:"";display:inline-block;width:2.5px;height:2.5px;background:var(--red);margin-right:2px;vertical-align:middle}
.card-dark{background:var(--black-card)}

/* letterheads */
.letter{width:222px;height:312px;top:24px}
.letter .head{position:absolute;top:18px;left:0;width:100%;text-align:center}
.letter .head .brand{font-size:11px;color:var(--ink)}
.letter .head .tag{font-size:4.4px;color:var(--muted);margin-top:2px;letter-spacing:.3px}
.letter .contact{position:absolute;top:14px;right:10px;font-size:3.8px;line-height:1.5;color:var(--muted)}
.letter .foot{position:absolute;bottom:8px;left:0;width:100%;font-size:4px;color:#fff;text-align:center}

/* envelopes */
.env{width:258px}
.env .brand{font-size:7px;color:var(--ink)}
.env .addr{font-size:4px;color:var(--muted)}
</style>
</head>
<body>
<main class="canvas">

  <section class="abs hero">
    <div class="brand">VANTOR CONSTRUCTION</div>
    <div class="tagline">TRUSTED BUILDING SERVICES</div>
    <div class="sub">Stationery Concepts</div>
  </section>

  <!-- option 1 back: services -->
  <article class="sheet card" style="left:12px;top:148px">
    <div class="services tiny">
      <span>Project Management</span><span>New Constructions</span>
      <span>Extensions</span><span>Renovations</span>
      <span>Kitchen Renovations</span><span>Bathroom Renovations</span>
      <span>Strata Works</span><span>Building Maintenance</span>
      <span>Insurance Works</span><span>Licensed &amp; Insured</span>
      <span>Member Of RTF</span><span>Member Of UTG</span>
    </div>
    <div class="abs tiny" style="left:8px;bottom:6px;color:var(--red);font-weight:600">One Call Gets It All.</div>
  </article>
  <div class="caption" style="left:12px;top:233px;width:152px">Option 1 Back</div>

  <!-- option 1 front -->
  <article class="sheet card" style="left:172px;top:148px">
    <svg class="swoosh" viewBox="0 0 152 82" preserveAspectRatio="none" aria-hidden="true">
      <path d="M84 0 Q112 36 152 34 L152 0Z" fill="var(--red)"/>
      <path d="M0 72 Q70 58 152 68 L152 82 L0 82Z" fill="var(--grey)"/>
    </svg>
    <div class="abs brand" style="left:7px;top:8px">VANTOR</div>
    <div class="abs tiny" style="left:7px;top:24px"><span class="name">Dean Holbrek</span><br>Director<br>P.O Box 481, Ferndale Ridge, NSW 1742<br>dean@vantorbuildco.com.au<br>www.vantorbuildco.com.au</div>
    <div class="abs tiny" style="right:6px;top:42px;text-align:right">Lic No: 371506K<br>ABN: 83207594116<br>ACN: 207594116</div>
    <div class="abs" style="right:8px;top:7px;width:12px;height:12px;background:#fff;border-radius:50%"></div>
  </article>
  <div class="caption" style="left:172px;top:233px;width:152px">Option 1 Front</div>

  <!-- option 2 front -->
  <article class="sheet card card-dark" style="left:12px;top:252px">
    <div class="abs brand" style="left:0;width:100%;text-align:center;top:24px;font-size:10px;color:#fff">VANTOR CONSTRUCTION</div>
    <div class="abs tiny" style="left:0;width:100%;text-align:center;top:38px;color:var(--red)">TRUSTED BUILDING SERVICES</div>
    <div class="abs tiny" style="left:0;width:100%;text-align:center;bottom:8px;color:#ccc">One Call Gets It All.</div>
  </article>
  <div class="caption" style="left:12px;top:337px;width:152px">Option 2 Front</div>

  <!-- option 2 back -->
  <article class="sheet card" style="left:172px;top:252px">
    <svg class="swoosh" viewBox="0 0 152 82" preserveAspectRatio="none" aria-hidden="true">
      <path d="M0 62 Q70 44 152 52 L152 82 L0 82Z" fill="var(--red)"/>
      <path d="M0 74 Q70 62 152 70 L152 82 L0 82Z" fill="var(--red-dark)"/>
    </svg>
    <div class="abs brand" style="left:7px;top:7px">VANTOR</div>
    <div class="abs tiny" style="left:7px;top:19px"><span class="name">Dean Holbrek</span><br>Director<br>dean@vantorbuildco.com.au<br>www.vantorbuildco.com.au</div>
    <div class="abs" style="right:9px;top:8px;width:16px;height:16px;background:var(--grey)"></div>
  </article>
  <div class="caption" style="left:172px;top:337px;width:152px">Option 2 Back</div>

  <!-- letterhead 1 -->
  <article class="sheet letter" style="left:336px">
    <div class="head"><div class="brand">VANTOR</div><div class="tag">TRUSTED BUILDING SERVICES</div></div>
    <div class="contact">P.O Box 481, Ferndale Ridge<br>NSW 1742<br>dean@vantorbuildco.com.au<br>www.vantorbuildco.com.au</div>
    <svg class="swoosh" viewBox="0 0 222 312" preserveAspectRatio="none" aria-hidden="true">
      <path d="M0 282 Q100 262 222 274 L222 312 L0 312Z" fill="var(--grey)"/>
      <path d="M0 292 Q110 276 222 286 L222 312 L0 312Z" fill="var(--red)"/>
    </svg>
    <div class="foot">www.vantorbuildco.com.au · ABN: 83207594116</div>
  </article>
  <div class="caption" style="left:336px;top:342px;width:222px">Letterhead Option 1</div>

  <!-- letterhead 2 -->
  <article class="sheet letter" style="left:600px">
    <div class="head"><div class="brand">VANTOR</div><div class="tag">TRUSTED BUILDING SERVICES</div></div>
    <svg class="swoosh" viewBox="0 0 222 312" preserveAspectRatio="none" aria-hidden="true">
      <path d="M0 266 Q110 292 222 262 L222 312 L0 312Z" fill="var(--red)"/>
      <path d="M0 286 Q110 304 222 282 L222 312 L0 312Z" fill="var(--red-dark)"/>
    </svg>
    <div class="foot">P.O Box 481, Ferndale Ridge, NSW 1742 · dean@vantorbuildco.com.au</div>
  </article>
  <div class="caption" style="left:600px;top:342px;width:222px">Letterhead Option 2</div>

  <!-- envelopes -->
  <article class="sheet env" style="left:869px;top:24px;height:70px;background:#6e6e6e">
    <svg class="swoosh" viewBox="0 0 258 70" preserveAspectRatio="none" aria-hidden="true">
      <path d="M0 0 L129 40 L258 0Z" fill="#f2f2f2"/>
    </svg>
    <div class="abs brand" style="left:0;width:100%;text-align:center;top:12px">VANTOR</div>
  </article>

  <article class="sheet env" style="left:869px;top:102px;height:76px">
    <svg class="swoosh" viewBox="0 0 258 76" preserveAspectRatio="none" aria-hidden="true">
      <path d="M0 0 L129 42 L258 0Z" fill="var(--red)"/>
    </svg>
    <div class="abs brand" style="left:0;width:100%;text-align:center;top:11px;color:#fff">VANTOR</div>
  </article>

  <article class="sheet env" style="left:869px;top:186px;width:240px;height:70px">
    <div class="abs brand" style="left:10px;top:9px">VANTOR</div>
    <div class="abs addr" style="left:10px;top:20px">P.O Box 481, Ferndale Ridge, NSW 1742</div>
    <svg class="swoosh" viewBox="0 0 240 70" preserveAspectRatio="none" aria-hidden="true">
      <path d="M0 58 Q120 46 240 56 L240 70 L0 70Z" fill="var(--red)"/>
    </svg>
  </article>

  <article class="sheet env" style="left:889px;top:264px;width:240px;height:84px">
    <div class="abs brand" style="left:10px;top:9px">VANTOR</div>
    <div class="abs addr" style="left:10px;top:20px">www.vantorbuildco.com.au</div>
    <svg class="swoosh" viewBox="0 0 240 84" preserveAspectRatio="none" aria-hidden="true">
      <path d="M0 64 Q120 52 240 62 L240 84 L0 84Z" fill="var(--grey)"/>
      <path d="M0 72 Q120 62 240 70 L240 84 L0 84Z" fill="var(--red)"/>
    </svg>
  </article>

</main>
</body>
</html>
```